Visitenkarten-Design für Unternehmensberatung
Zielgruppe
Das Unternehmen BAK Baltisch-Andines Kooperationsnetz UG berät Firmen aus dem Orient bei Geschäftsaktivitäten und Projekten.
Aufgabenstellung
Die Visitenkarte sollte Seriosität und einen leicht orientalischen Eindruck machen.

```html
<!DOCTYPE html>
<html lang="de">
<head>
<meta charset="utf-8">
<title>BAK Visitenkarte</title>
<link rel="stylesheet" href="https://fonts.googleapis.com/css2?family=PT+Sans:wght@400;700&display=swap">
<style>
  :root {
    --brand-blue: #0f56a8;
    --ink-grey: #5a5a5a;
    --edge-grey: #9a9ca3;
    --paper: #ffffff;
    --backdrop: #ecebe8;
  }
  * { margin: 0; padding: 0; box-sizing: border-box; }
  html, body { width: 1200px; height: 892px; overflow: hidden; }
  body {
    background: var(--backdrop);
    font-family: "PT Sans", sans-serif;
    display: flex;
    align-items: center;
    justify-content: center;
    gap: 56px;
  }
  .card {
    position: relative;
    width: 520px;
    height: 316px;
    border-radius: 4px;
    overflow: hidden;
    box-shadow: 0 8px 24px rgba(0,0,0,.14);
  }
  .card--front { background: var(--paper); }
  .card--back {
    background: var(--brand-blue);
    display: flex;
    align-items: center;
    justify-content: center;
  }
  .brand { display: flex; align-items: center; gap: 14px; }
  .brand__mark {
    font-weight: 700;
    font-size: 26px;
    letter-spacing: .5px;
  }
  .brand__name {
    font-weight: 700;
    font-size: 19px;
    line-height: 1.02;
  }
  .card--front .brand { position: absolute; left: 30px; top: 30px; color: var(--brand-blue); }
  .card--back .brand { color: var(--paper); }
  .card--back .brand__mark { font-size: 30px; }
  .card--back .brand__name { font-size: 22px; }
  .contact {
    position: absolute;
    left: 34px;
    top: 140px;
    list-style: none;
    color: var(--ink-grey);
    font-size: 15px;
    line-height: 1.3;
  }
  .contact li { display: flex; align-items: flex-start; gap: 8px; }
  .contact svg { width: 14px; height: 14px; margin-top: 3px; flex: none; fill: var(--ink-grey); }
  .contact .indent { padding-left: 22px; }
  .person {
    position: absolute;
    right: 34px;
    bottom: 58px;
    text-align: left;
  }
  .person__name { color: var(--brand-blue); font-weight: 700; font-size: 17px; }
  .person__role { color: var(--ink-grey); font-size: 14px; }
  .edge-band {
    position: absolute;
    left: 0; bottom: 0;
    width: 100%; height: 22px;
  }
</style>
</head>
<body>
  <section class="card card--front" aria-label="Vorderseite">
    <div class="brand">
      <span class="brand__mark">BAK</span>
      <span class="brand__name">Baltisch-<br>Andines<br>Kooperationsnetz UG</span>
    </div>
    <ul class="contact">
      <li><svg viewBox="0 0 14 14"><path d="M7 0a5 5 0 0 0-5 5c0 3.5 5 9 5 9s5-5.5 5-9a5 5 0 0 0-5-5zm0 7a2 2 0 1 1 0-4 2 2 0 0 1 0 4z"/></svg>: Kleine Mühlenstraße 9</li>
      <li class="indent">20459 Hamburg</li>
      <li><svg viewBox="0 0 14 14"><path d="M3 1l2.5 3-1.3 1.4a8 8 0 0 0 4.4 4.4L10 8.5l3 2.5-1.5 2.2C6 13 1 8 .8 2.5z"/></svg>: +49 40 512093</li>
      <li><svg viewBox="0 0 14 14"><path d="M1 5h12v7H1zM3 2h8v3H3zM3 7h2v1H3zm3 0h2v1H6zm3 0h2v1H9z"/></svg>: +49 40 51209377</li>
    </ul>
    <div class="person">
      <p class="person__name">Leyla Hartmann</p>
      <p class="person__role">Geschäftsführerin</p>
    </div>
    <svg class="edge-band" viewBox="0 0 520 22" preserveAspectRatio="none" aria-hidden="true">
      <polygon points="0,4 360,4 372,22 0,22" fill="var(--brand-blue)"/>
      <polygon points="372,22 382,10 520,10 520,22" fill="var(--edge-grey)"/>
    </svg>
  </section>

  <section class="card card--back" aria-label="Rückseite">
    <div class="brand">
      <span class="brand__mark">BAK</span>
      <span class="brand__name">Baltisch-<br>Andines<br>Kooperationsnetz UG</span>
    </div>
  </section>
</body>
</html>
```